Stationery design for law/Property/finance business

We need stationery design for a Law/Property/Finance business called Stonebridge. Logo is attached.
we require a letterhead and with compliments slip.
Would like to see a very simple professional design using the colours of the logo and offset against Charcoal colours. Maybe a charcoal band for header and footer with logo and details appearing in it? Former letterhead attached for examples.
we require the project to be provided in word, pdf and jpeg format.
we require the following details on the stationery:
Cairns Phone: 07 41592036
Weipa Phone: 07 41357904
Mobile: 0427 915 384
Fax: 07 41836257
email: admin@stonebridgeholdings.com.au
ABN 52 304 781 619

```html
<!DOCTYPE html>
<html lang="en">
<head>
<meta charset="utf-8">
<title>Stonebridge Stationery</title>
<link rel="stylesheet" href="https://fonts.googleapis.com/css2?family=Montserrat:wght@400;600;700&family=Bubblegum+Sans&display=swap">
<style>
  :root {
    --board: #b8b8b8;
    --charcoal: #222222;
    --paper: #ffffff;
    --brand-blue: #2a8fd6;
    --ink-light: #e6e6e6;
    --accent-script: #1f6fba;
    --faint-blue: #dbeaf5;
  }
  * { margin: 0; padding: 0; box-sizing: border-box; }
  html, body { width: 1200px; height: 1200px; overflow: hidden; }
  body {
    background: var(--board);
    font-family: "Montserrat", Arial, sans-serif;
    position: relative;
  }
  .sheet {
    position: absolute;
    background: var(--paper);
    box-shadow: 8px 10px 10px rgba(0,0,0,0.45);
    overflow: hidden;
  }
  .letterhead { left: 334px; top: 79px; width: 517px; height: 733px; }
  .slip { left: 293px; top: 848px; width: 614px; height: 289px; }

  .band { position: absolute; left: 0; right: 0; background: var(--charcoal); color: var(--ink-light); }
  .letterhead .header-band { top: 0; height: 98px; }
  .letterhead .footer-band { top: 697px; height: 16px; }
  .slip .header-band { top: 0; height: 90px; }

  .brand-name {
    position: absolute;
    font-family: "Montserrat", Arial, sans-serif;
    font-weight: 700;
    color: var(--brand-blue);
    letter-spacing: 0.5px;
    display: flex; align-items: center; gap: 6px;
  }
  .brand-name .mark { width: 10px; height: 10px; border-radius: 50%; background: var(--brand-blue); }
  .letterhead .brand-name { left: 46px; top: 36px; font-size: 21px; }
  .slip .brand-name { left: 34px; top: 34px; font-size: 19px; }

  .contact { font-size: 7.4px; line-height: 1; white-space: nowrap; }
  .contact-line { display: flex; align-items: center; gap: 4px; height: 11px; }
  .contact-line svg { width: 7px; height: 7px; fill: var(--ink-light); flex: none; }

  .letterhead .header-contact {
    position: absolute; left: 331px; top: 41px;
    border-left: 1px solid #777; padding-left: 10px; padding-top: 1px;
  }
  .letterhead .header-contact .abn { margin-top: 6px; font-size: 7.6px; }

  .footer-band .contact-row {
    position: absolute; left: 68px; top: 4px;
    display: flex; gap: 22px;
  }
  .footer-band .contact-line { height: 8px; }

  .slip .contact-col { position: absolute; top: 48px; }
  .slip .col-mobile { left: 201px; }
  .slip .col-phones { left: 297px; top: 46px; }
  .slip .col-web { left: 430px; top: 46px; }
  .slip .contact { font-size: 8px; }
  .slip .contact-line { height: 13px; }

  .faint-motif {
    position: absolute; border-radius: 50%;
    background: var(--faint-blue); opacity: 0.7;
  }
  .letterhead .faint-motif { left: 50px; top: 445px; width: 210px; height: 210px; }
  .slip .faint-motif { left: 420px; top: 130px; width: 130px; height: 130px; }

  .compliments {
    position: absolute; right: 18px; bottom: 14px;
    font-family: "Bubblegum Sans", "Comic Sans MS", cursive;
    font-size: 24px; color: var(--accent-script);
  }
</style>
</head>
<body>

<svg width="0" height="0" style="position:absolute">
  <defs>
    <symbol id="icon-mail" viewBox="0 0 10 10"><path d="M0 3l5 3 5-3v7H0z M1 2h8L5 4.5z"/></symbol>
    <symbol id="icon-web" viewBox="0 0 10 10"><path d="M5 0a5 5 0 1 0 0 10A5 5 0 0 0 5 0zm0 1a4 4 0 0 1 0 8 4 4 0 0 1 0-8zM1 4.5h8v1H1zM4.5 1h1v8h-1z"/></symbol>
    <symbol id="icon-mobile" viewBox="0 0 10 10"><path d="M3 0h4v10H3zm1 1v6h2V1z"/></symbol>
    <symbol id="icon-fax" viewBox="0 0 10 10"><path d="M3 0h5v4H3zM1 4h8v6H1zm2 2v1h1V6zm2 0v1h1V6z"/></symbol>
    <symbol id="icon-phone" viewBox="0 0 10 10"><path d="M0 3c0-2 10-2 10 0v1H7V3H3v1H0zM2 5h6l1 4H1z"/></symbol>
  </defs>
</svg>

<section class="sheet letterhead" aria-label="Letterhead">
  <header class="band header-band">
    <div class="brand-name"><span class="mark"></span>STONEBRIDGE</div>
    <div class="header-contact contact">
      <div class="contact-line"><svg><use href="#icon-mail"/></svg>admin@stonebridgeholdings.com.au</div>
      <div class="contact-line"><svg><use href="#icon-web"/></svg>www.stonebridgeholdings.com.au</div>
      <div class="abn">ABN 52 304 781 619</div>
    </div>
  </header>

  <div class="faint-motif" role="img" aria-label="Faint brand watermark"></div>

  <footer class="band footer-band">
    <div class="contact-row contact">
      <div class="contact-line"><svg><use href="#icon-mobile"/></svg>0427 915 384</div>
      <div class="contact-line"><svg><use href="#icon-fax"/></svg>07 41836257</div>
      <div class="contact-line"><svg><use href="#icon-phone"/></svg>07 41592036 &nbsp;(Cairns)</div>
      <div class="contact-line"><svg><use href="#icon-phone"/></svg>07 41357904 &nbsp;(Weipa)</div>
    </div>
  </footer>
</section>

<section class="sheet slip" aria-label="With compliments slip">
  <header class="band header-band">
    <div class="brand-name"><span class="mark"></span>STONEBRIDGE</div>
    <div class="contact-col col-mobile contact">
      <div class="contact-line"><svg><use href="#icon-mobile"/></svg>0427 915 384</div>
      <div class="contact-line"><svg><use href="#icon-fax"/></svg>07 41836257</div>
    </div>
    <div class="contact-col col-phones contact">
      <div class="contact-line"><svg><use href="#icon-phone"/></svg>07 41592036 &nbsp;(Cairns)</div>
      <div class="contact-line"><svg><use href="#icon-phone"/></svg>07 41357904 &nbsp;(Weipa)</div>
    </div>
    <div class="contact-col col-web contact">
      <div class="contact-line"><svg><use href="#icon-mail"/></svg>admin@stonebridgeholdings.com.au</div>
      <div class="contact-line"><svg><use href="#icon-web"/></svg>www.stonebridgeholdings.com.au</div>
    </div>
  </header>

  <div class="faint-motif" role="img" aria-label="Faint brand watermark"></div>
  <div class="compliments">With Compliments</div>
</section>

</body>
</html>
```